Branvique needs a business Card Design

We are looking for a business card Design for our new Managed Service Provider Company, Branvique. Branvique encompasses everything IT for the average medium sized business. Our primary services are help desk support, cyber-security (malware and ransomware protection), and Disaster Recovery systems. We would like the design to have a very clean and professional look, with a very minimalist feel.

Target Market(s)

Medium to large sized businesses

Industry/Entity Type

It Service

Contact Information for Business Card

Name GoesHere
name@branvique.com
O: 555-382-6047
C: 555-731-5820

Font styles to use
Other font styles liked:
• Poppins Font Only Please

Colors

Designer to choose only greyscale colors for use in the design.

Requirements
Must have
• Logo included
Nice to have
• Cutting Edge, innovative, minimalistic, elegant

```html
<!DOCTYPE html>
<html lang="en">
<head>
<meta charset="utf-8">
<title>Branvique — Business Card</title>
<link rel="stylesheet" href="https://fonts.googleapis.com/css2?family=Poppins:wght@300;400;500;600&display=swap">
<style>
  :root {
    --page-bg: #e9e9e9;
    --card-black: #141414;
    --card-black-edge: #262626;
    --card-white: #ffffff;
    --ink-dark: #2b2b2b;
    --ink-mid: #555555;
    --ink-soft: #7a7a7a;
    --logo-on-dark: #5f5f5f;
    --rule: #3a3a3a;
  }
  * { box-sizing: border-box; margin: 0; padding: 0; }
  html, body {
    width: 1200px; height: 1200px; overflow: hidden;
    background: var(--page-bg);
    font-family: "Poppins", sans-serif;
  }
  .sheet {
    width: 1200px; height: 1200px;
    display: flex; flex-direction: column;
    align-items: center; justify-content: center; gap: 70px;
  }
  .card {
    position: relative;
    width: 735px; height: 420px;
    box-shadow: 0 14px 34px rgba(0,0,0,0.18);
  }

  /* Front */
  .card-front {
    background: linear-gradient(150deg, var(--card-black-edge) 0%, var(--card-black) 55%, #0c0c0c 100%);
    display: flex; align-items: center; justify-content: center;
  }
  .front-wordmark {
    font-weight: 400; font-size: 52px; letter-spacing: 0.34em;
    color: var(--logo-on-dark); text-transform: uppercase;
    margin-right: -0.34em;
  }

  /* Back */
  .card-back { background: var(--card-white); color: var(--ink-dark); }
  .back-wordmark {
    position: absolute; top: 92px; right: 70px;
    font-weight: 400; font-size: 22px; letter-spacing: 0.3em;
    color: var(--ink-mid); text-transform: uppercase;
  }
  .identity {
    position: absolute; left: 62px; top: 222px;
    padding-left: 14px; border-left: 2px solid var(--rule);
    line-height: 1.25;
  }
  .identity-name { font-weight: 600; font-size: 15px; color: var(--ink-dark); }
  .identity-role { font-weight: 400; font-size: 13px; color: var(--ink-soft); }
  .contact-list {
    position: absolute; left: 62px; top: 300px;
    list-style: none; display: flex; flex-direction: column; gap: 9px;
  }
  .contact-item, .address {
    display: flex; align-items: center; gap: 9px;
    font-size: 14px; font-weight: 400; color: var(--ink-dark);
  }
  .address { position: absolute; left: 320px; top: 332px; }
  .icon { width: 20px; height: 20px; flex: none; }
</style>
</head>
<body>
<main class="sheet">

  <section class="card card-front" aria-label="Card front">
    <span class="front-wordmark">Branvique</span>
  </section>

  <section class="card card-back" aria-label="Card back">
    <span class="back-wordmark">Branvique</span>

    <div class="identity">
      <p class="identity-name">Name</p>
      <p class="identity-role">President</p>
    </div>

    <ul class="contact-list">
      <li class="contact-item">
        <svg class="icon" viewBox="0 0 20 20" aria-hidden="true">
          <circle cx="10" cy="10" r="10" fill="#2b2b2b"/>
          <path d="M7 5.5l1.6 0 .8 2.2-1 .9c.5 1.1 1.3 1.9 2.4 2.4l.9-1 2.2.8v1.6c0 .5-.4.9-.9.9C9.6 13.3 6.7 10.4 6.1 6.4c0-.5.4-.9.9-.9z" fill="#fff"/>
        </svg>
        (555) 382 6047
      </li>
      <li class="contact-item">
        <svg class="icon" viewBox="0 0 20 20" aria-hidden="true">
          <circle cx="10" cy="10" r="10" fill="#2b2b2b"/>
          <rect x="5" y="6.5" width="10" height="7" rx="1" fill="none" stroke="#fff" stroke-width="1.3"/>
          <path d="M5.4 7l4.6 3.6L14.6 7" fill="none" stroke="#fff" stroke-width="1.3"/>
        </svg>
        name@branvique.com
      </li>
      <li class="contact-item">
        <svg class="icon" viewBox="0 0 20 20" aria-hidden="true">
          <circle cx="10" cy="10" r="10" fill="#2b2b2b"/>
          <circle cx="10" cy="10" r="5" fill="none" stroke="#fff" stroke-width="1.2"/>
          <ellipse cx="10" cy="10" rx="2.2" ry="5" fill="none" stroke="#fff" stroke-width="1.1"/>
          <path d="M5 10h10" stroke="#fff" stroke-width="1.1"/>
        </svg>
        www.branvique.com
      </li>
    </ul>

    <p class="address">
      <svg class="icon" viewBox="0 0 20 20" aria-hidden="true">
        <circle cx="10" cy="10" r="10" fill="#2b2b2b"/>
        <path d="M10 4.5c-2 0-3.5 1.5-3.5 3.4 0 2.6 3.5 6.6 3.5 6.6s3.5-4 3.5-6.6c0-1.9-1.5-3.4-3.5-3.4z" fill="#fff"/>
        <circle cx="10" cy="8" r="1.2" fill="#2b2b2b"/>
      </svg>
      4120, 9th Avenue, Lakeview NY 10482
    </p>
  </section>

</main>
</body>
</html>
```